Customer Brochure for Startup Managed IT Security Provider

We would like to have a distinctive brochure that presents the key facts about our offering in a simple and easy to read brochure.

I have roughed out a couple of examples showing the information but we are looking for something completely different to that. The information in the 2 is slightly different but if we are able to edit the text in the final versions we can do that ourselves.

I have uploaded our log also, that will most likely dictate the colour scheme so the logo colour should be the overriding colour but it would be nice to see variations throughout.

The design should look and feel fresh but ultimately we want the reader to feel safe and secured.

Target Market(s)

Our target market is sub 200 user businesses across all sectors but we will need to appeal to enterprise customers also.

Industry/Entity Type

Computer Security

Font styles to use
Serif

Requirements
Nice to have
• Would be nice to have a fluid feel to it.

```html
<!DOCTYPE html>
<html lang="en">
<head>
<meta charset="utf-8">
<title>Warden 360 – Managed Security Brochure</title>
<link rel="stylesheet" href="https://fonts.googleapis.com/css2?family=Open+Sans:wght@400;600;700&family=Ubuntu:wght@500;700&display=swap">
<style>
  :root {
    --navy: #2b2f6e;
    --sky: #289fda;
    --sky-light: #2fa6e6;
    --ink: #222226;
    --paper: #ffffff;
    --backdrop: #ece8e2;
    --image-light: #f4f1ea;
    --image-mid: #e2ddd2;
    --image-dark: #cfcac0;
  }
  * { box-sizing: border-box; margin: 0; padding: 0; }
  html, body {
    width: 1200px; height: 1200px; overflow: hidden;
    background: var(--backdrop);
  }
  .stage { position: relative; width: 1200px; height: 1200px; }
  .page {
    position: absolute; left: 197px; top: 30px;
    width: 938px; height: 1326px;
    transform: scale(0.86); transform-origin: 0 0;
    background: var(--paper);
    box-shadow: 0 6px 22px rgba(0,0,0,.18);
    font-family: "Open Sans", sans-serif;
    color: var(--ink);
    overflow: hidden;
  }
  .masthead { position: absolute; right: 0; top: 0; width: 500px; height: 53px; }
  .masthead svg { position: absolute; inset: 0; }
  .masthead__name {
    position: absolute; left: 76px; top: 9px;
    font-family: "Ubuntu", sans-serif; font-weight: 500;
    font-size: 30px; color: #fff; letter-spacing: .3px;
  }
  .column { position: absolute; top: 106px; width: 390px; }
  .column--problem { left: 53px; }
  .column--benefits { left: 495px; }
  .heading {
    font-family: "Ubuntu", sans-serif; font-weight: 700;
    color: var(--navy); line-height: 1.1;
  }
  .heading--problem { font-size: 27px; margin-top: 4px; margin-bottom: 18px; }
  .heading--benefits { font-size: 28px; margin: 24px 0 25px; letter-spacing: .4px; }
  .lead {
    font-weight: 700; font-size: 18.5px; line-height: 21px;
    letter-spacing: -.5px; margin-bottom: 21px;
  }
  .copy {
    font-size: 18.5px; line-height: 21px; letter-spacing: -.4px;
    text-align: justify; margin-bottom: 21px;
  }
  .feature-image {
    width: 385px; height: 235px;
    background: linear-gradient(135deg, var(--image-mid) 0%, var(--image-light) 45%, var(--image-light) 60%, var(--image-dark) 100%);
  }
  .solution {
    position: absolute; left: 0; top: 800px; width: 938px; height: 526px;
    background: var(--sky);
    color: #fff;
  }
  .solution__bar {
    position: absolute; left: 53px; top: 0; width: 832px; height: 54px;
    background: var(--navy); border-radius: 0 0 8px 8px;
    font-family: "Ubuntu", sans-serif; font-weight: 700;
    font-size: 27px; letter-spacing: .8px;
    display: flex; align-items: center; justify-content: center;
  }
  .solution__body { position: absolute; left: 53px; top: 93px; width: 832px; }
  .solution__body .copy { margin-bottom: 21px; }
  .solution__body .copy--tight { margin-bottom: 0; }
  .cta { font-weight: 700; font-size: 18.5px; line-height: 21px; letter-spacing: -.2px; }
  .cta__url { font-size: 25px; letter-spacing: .2px; }
</style>
</head>
<body>
<div class="stage">
  <article class="page">
    <header class="masthead">
      <svg width="500" height="53" viewBox="0 0 500 53" aria-hidden="true">
        <polygon points="0,53 24,0 58,0 34,53" fill="var(--sky-light)"/>
        <polygon points="34,53 58,0 500,0 500,53" fill="var(--navy)"/>
      </svg>
      <span class="masthead__name">Norvane Systems Limited</span>
    </header>

    <section class="column column--problem">
      <h2 class="heading heading--problem">Is the problem that big?</h2>
      <p class="lead">You are exposed to a growing number<br>of zero day threats each and every day.</p>
      <p class="copy">Malware is becoming more and more advanced and is also becoming much more targeted. With delivery methods becoming more advanced also the chance of you encountering a threat is ever increasing.</p>
      <p class="copy">With traditional AV solutions unable to detect much of this malware you are facing a problem you are unable to see and unable to defend against.</p>
      <p class="copy">Do you know if you have suffered a breach or attack? With many unable to afford or run the advanced detection and forensics tools many are in the dark as to how big the problem is.</p>
      <p class="copy">In the event of a breach or even just a ransomware attack on the network, how much of your time will be involved in searching for and finding remediation tools?</p>
      <p class="copy">Do you have the time to manage the problem?</p>
    </section>

    <section class="column column--benefits">
      <div class="feature-image" role="img" aria-label="Photo of a magnified dictionary entry defining the word benefits"></div>
      <h2 class="heading heading--benefits">“What are the benefits<br>to you?”</h2>
      <p class="copy">Monthly billing options allows you to pay as you go and protect what you need to protect.</p>
      <p class="copy">Flexibility in billing allows you to manage your budget to suit you.</p>
      <p class="copy">No longer do you have to pay for licenses you aren’t using, only active licenses are billed each month.</p>
      <p class="copy">No more time spent managing or updating your protection and most importantly, no more worrying about it.</p>
    </section>

    <section class="solution">
      <h2 class="solution__bar">WHAT IS THE SOLUTION AND HOW DOES IT WORK?</h2>
      <div class="solution__body">
        <p class="copy">Warden 360 is powered by Norvane Systems Limited allowing us to centrally manage your endpoints. Our analysts get alerted to all threats as soon as they are detected by our behavioural analysis agent and they are trained to analyse the threat quickly and effectively.</p>
        <p class="copy">When threats are detected, we are able to stop them in their tracks regardless of whether they are conventional malware, file less, browser or network threats ensuring the safety of your users.</p>
        <p class="copy copy--tight">A report follows after detection detailing the threat and what actions have been taken and what remediation steps have been taken too.</p>
        <p class="copy">In the event of a ransomware attack that did manage to encrypt some files before being stopped, we can recover files in a matter of seconds, returning them to the exact state they were in prior to encryption.</p>
        <p class="cta">To find out more visit <span class="cta__url">www.warden360.net</span><br>to find out more and sign up today.</p>
      </div>
    </section>
  </article>
</div>
</body>
</html>
```